Brightwell Amusements Investor Brochure

Start Up Company Brightwell Amusements requires 4 page A4 size brochure outlining and detailing new product. Draft layout attached. Information and points of difference included. Company logo and graphics attached. Final design should sell to investors.

```html
<!DOCTYPE html>
<html lang="en">
<head>
<meta charset="utf-8">
<title>Brightwell Amusements – Investor Brochure</title>
<link href="https://fonts.googleapis.com/css2?family=Roboto+Condensed:wght@400;700&family=Roboto:wght@400;700&display=swap" rel="stylesheet">
<style>
  :root {
    --sky: #1ab6ef;
    --sky-deep: #0f8fd8;
    --sky-light: #35c6f4;
    --paper: #ffffff;
    --mist: #e6e7e9;
    --mist-light: #f7f7f8;
    --ink: #555659;
    --brand: #1b6fb3;
    --frame: #d6d7d9;
  }
  * { margin: 0; padding: 0; box-sizing: border-box; }
  html, body { width: 1200px; height: 1000px; overflow: hidden; background: var(--paper); }
  body { position: relative; font-family: "Roboto", Arial, sans-serif; }

  .page { position: absolute; top: 131px; width: 497px; height: 702px; overflow: hidden; }
  .page--hospitals { left: 101px; border: 1px solid var(--frame);
    background: linear-gradient(180deg, var(--mist-light) 50%, var(--mist) 100%); }
  .page--travellers { left: 607px;
    background: linear-gradient(180deg, var(--mist) 0%, var(--mist-light) 45%); }

  .band { position: absolute; background: linear-gradient(90deg, var(--sky-light), var(--sky-deep)); }
  .page--hospitals .band { left: 0; top: 0; width: 497px; height: 226px; }
  .page--travellers .band { left: 0; top: 480px; width: 497px; height: 222px;
    background: linear-gradient(90deg, var(--sky-deep), var(--sky-light)); }

  .photo { position: absolute; }
  .photo--hospital { left: 0; top: 195px; width: 497px; height: 177px;
    clip-path: polygon(132px 0, 497px 0, 497px 177px, 0 177px, 0 31px, 132px 31px);
    background: linear-gradient(180deg, #b9b6b1 0%, #d7d6d2 25%, #8f969d 55%, #3f4650 100%); }
  .photo--concourse { left: 0; top: 195px; width: 497px; height: 315px;
    clip-path: polygon(132px 0, 497px 0, 497px 285px, 365px 285px, 365px 315px, 0 315px, 0 31px, 132px 31px);
    background: linear-gradient(180deg, #5d6a7c 0%, #9fb0c6 35%, #c9d2dd 60%, #8a97a8 100%); }

  .headline { position: absolute; color: var(--paper); font-family: "Roboto Condensed", "Arial Narrow", sans-serif; }
  .page--hospitals .headline { left: 72px; top: 58px; }
  .headline__title { font-size: 25px; font-weight: 400; line-height: 32px; padding-bottom: 4px;
    border-bottom: 1px solid rgba(255,255,255,.55); display: inline-block; }
  .page--hospitals .headline__title { width: 200px; }
  .headline__sub { font-size: 21px; line-height: 24px; margin-top: 10px; }
  .headline__points { font-family: "Roboto", Arial, sans-serif; font-weight: 700; font-size: 15px; line-height: 17px; }

  .page--travellers .headline { left: 64px; top: 557px; }
  .page--travellers .headline__title { font-size: 31px; font-weight: 700; line-height: 32px; border: 0; padding: 0; }
  .page--travellers .headline__sub { font-size: 22px; font-weight: 700; margin-top: -3px; width: 345px;
    padding-bottom: 4px; border-bottom: 1px solid rgba(255,255,255,.45); }
  .page--travellers .headline__points { font-weight: 400; font-size: 14px; margin-top: 5px; }

  .table-title { position: absolute; left: 60px; top: 395px; font-family: "Roboto Condensed", "Arial Narrow", sans-serif;
    font-size: 15px; color: var(--ink); }
  .stats { position: absolute; left: 60px; top: 425px; width: 394px; height: 147px;
    background: linear-gradient(90deg, var(--sky-light), var(--sky-deep));
    border-collapse: collapse; color: var(--paper); font-family: "Roboto Condensed", "Arial Narrow", sans-serif;
    font-size: 8px; table-layout: fixed; }
  .stats td, .stats th { text-align: center; height: 12.3px; padding: 0; font-weight: 400; }
  .stats th { font-weight: 700; height: 18px; }
  .stats .label { text-align: right; padding-right: 4px; width: 154px; }
  .stats td:not(.label), .stats th:not(.label) { border-left: 2px solid rgba(255,255,255,.9); }
  .stats tr.gap td { height: 12px; }

  .kiosk { position: absolute; background: linear-gradient(180deg, #2d3a55 0%, #1f5fb0 70%, #1a2a45 100%); border-radius: 6px 14px 2px 2px; }
  .kiosk--hospital { left: 64px; top: 539px; width: 71px; height: 122px; }
  .kiosk--concourse { left: 108px; top: 320px; width: 80px; height: 182px; }

  .brand { position: absolute; display: flex; align-items: center; gap: 8px; color: var(--brand);
    font-family: "Roboto Condensed", "Arial Narrow", sans-serif; font-weight: 700; }
  .brand__mark { width: 22px; height: 22px; background: var(--brand); border-radius: 3px; flex: none; }
  .brand__name { line-height: 1; }
  .brand--small { left: 338px; top: 624px; font-size: 13px; }
  .brand--large { left: 126px; top: 72px; font-size: 27px; gap: 14px; }
  .brand--large .brand__mark { width: 44px; height: 44px; border-radius: 6px; }
</style>
</head>
<body>

<section class="page page--hospitals">
  <div class="band"></div>
  <div class="headline">
    <h1 class="headline__title">Movies in Hospitals</h1>
    <p class="headline__sub">Download Movies</p>
    <p class="headline__points">in under 3 minutes<br>No Internet Connection Required</p>
  </div>
  <div class="photo photo--hospital" role="img" aria-label="Photograph of a modern hospital building with a car park under a cloudy sky"></div>

  <h2 class="table-title">Public and Private Hospitals, States and Territories, 2012-13</h2>
  <table class="stats">
    <tr><th class="label"></th><th>NSW</th><th>Vic</th><th>Qld</th><th>WA</th><th>SA</th><th>Tas</th><th>ACT</th><th>NT</th><th>Total</th></tr>
    <tr><td class="label">Public hospitals</td><td></td><td></td><td></td><td></td><td></td><td></td><td></td><td></td><td></td></tr>
    <tr><td class="label">Public acute hospitals</td><td>218</td><td>149</td><td>166</td><td>88</td><td>78</td><td>22</td><td>3</td><td>5</td><td>729</td></tr>
    <tr><td class="label">Public psychiatric hospitals</td><td>7</td><td>1</td><td>4</td><td>2</td><td>2</td><td>1</td><td>. .</td><td>. .</td><td>17</td></tr>
    <tr><td class="label">Total public hospitals</td><td>225</td><td>150</td><td>170</td><td>90</td><td>80</td><td>23</td><td>3</td><td>5</td><td>746</td></tr>
    <tr><td class="label">Private hospitals</td><td></td><td></td><td></td><td></td><td></td><td></td><td></td><td></td><td></td></tr>
    <tr><td class="label">Private free-standing day hospital facilities</td><td>96</td><td>85</td><td>52</td><td>35</td><td>26</td><td>0</td><td>0</td><td>0</td><td>311</td></tr>
    <tr><td class="label">Other private hospitals</td><td>89</td><td>79</td><td>53</td><td>22</td><td>28</td><td>0</td><td>0</td><td>0</td><td>281</td></tr>
    <tr><td class="label">Total private hospitals</td><td>185</td><td>164</td><td>105</td><td>57</td><td>54</td><td>0</td><td>0</td><td>0</td><td>592</td></tr>
    <tr class="gap"><td class="label"></td><td></td><td></td><td></td><td></td><td></td><td></td><td></td><td></td><td></td></tr>
    <tr><td class="label">All hospitals</td><td>410</td><td>314</td><td>275</td><td>147</td><td>134</td><td>0</td><td>0</td><td>0</td><td>1,338</td></tr>
  </table>

  <div class="kiosk kiosk--hospital" role="img" aria-label="Render of the curved movie download kiosk"></div>

  <div class="brand brand--small">
    <span class="brand__mark"></span>
    <span class="brand__name">BRIGHTWELL<br>AMUSEMENTS</span>
  </div>
</section>

<section class="page page--travellers">
  <div class="brand brand--large">
    <span class="brand__mark"></span>
    <span class="brand__name">BRIGHTWELL<br>AMUSEMENTS</span>
  </div>
  <div class="photo photo--concourse" role="img" aria-label="Photograph of a bright airport concourse with travellers and a download kiosk"></div>
  <div class="band"></div>
  <div class="headline">
    <h1 class="headline__title">Movies for Travellers</h1>
    <p class="headline__sub">Download Movies in under 3 minutes</p>
    <p class="headline__points">No Internet Connection Required.</p>
  </div>
</section>

</body>
</html>
```